Logo + Label Design (Men’s Grooming Brand & Product Packaging)

Design a logo and 2 oz pomade label for Brant, a modern men’s grooming brand focused on clean, high-quality, natural ingredients. The design should establish a bold, masculine, minimalist identity that can later extend to products like shaving gel and body wash.

Key Requirements

Create a primary logo for “Brant” and a core label for the 2 oz pomade jar (screw-top).

Use a clean, modern style — masculine, confident, and approachable (think Wendel’s, Valto, Northfield Mill).

Design for 1–2 color screen printing on solid jar colors (white, black, or navy).

Avoid gradients, foil, or embossing. Must work in black & white.

Provide: vector logo, mockup of the 2 oz jar, color palette (CMYK/RGB/HEX), and font specs.

Winning design may lead to future projects (body wash, shave gel, skincare lines).

Font styles to use
Other font styles liked:
• We like the fonts and design concept in the attached mockup.

Requirements
Should not have
• We want to avoid too much writing or busy designs. We want to avoid having graphics/illustrations embedded in the logo if they will cause the brand to look less classy or sophisticated. We also want the design to look simple and all-American (e.g. Pellham and Stroud, Tall Pine, The BRIM, etc). We’d like to give a Kessler & Dunmore vibe that feels classy and high end.

```html
<!DOCTYPE html>
<html lang="en">
<head>
<meta charset="utf-8">
<title>Brant Hair Pomade Label</title>
<link href="https://fonts.googleapis.com/css2?family=Inter:wght@400;500&display=swap" rel="stylesheet">
<style>
  :root {
    --ink: #1b1a33;
    --canvas: #f8f8f8;
    --label: #ffffff;
    --edge: #e3e3e6;
  }
  * { margin: 0; padding: 0; box-sizing: border-box; }
  html, body { width: 1200px; height: 1000px; overflow: hidden; }
  body {
    position: relative;
    background: var(--canvas);
    font-family: "Inter", sans-serif;
    color: var(--ink);
  }
  .side-label {
    position: absolute;
    left: 146px; top: 517px;
    width: 397px; height: 106px;
    background: var(--label);
    border: 1px solid var(--edge);
    border-radius: 10px;
  }
  .side-label .wordmark {
    position: absolute;
    left: 34px; top: 36px;
    font-size: 28px;
    font-weight: 500;
    letter-spacing: 3px;
    line-height: 1;
  }
  .side-label .divider {
    position: absolute;
    left: 157px; top: 40px;
    width: 1px; height: 37px;
    background: var(--ink);
  }
  .side-label .claims {
    position: absolute;
    left: 163px; top: 38px;
    list-style: none;
    font-size: 10px;
    line-height: 15px;
    letter-spacing: -0.1px;
  }
  .lid-label {
    position: absolute;
    left: 676px; top: 330px;
    width: 374px; height: 374px;
    border-radius: 50%;
    background: var(--label);
    border: 1px solid var(--edge);
    text-align: center;
  }
  .lid-label .wordmark {
    position: absolute;
    left: 0; right: 0; top: 112px;
    font-size: 50px;
    font-weight: 500;
    letter-spacing: 6px;
    line-height: 1;
  }
  .lid-label .product {
    position: absolute;
    left: 0; right: 0; top: 204px;
    font-size: 23px;
    font-weight: 500;
    letter-spacing: -0.6px;
    line-height: 1;
  }
  .lid-label .scent {
    position: absolute;
    left: 0; right: 0; top: 232px;
    font-size: 19px;
    font-weight: 400;
    line-height: 1;
  }
  .lid-label .rule {
    position: absolute;
    left: 105px; top: 257px;
    width: 160px; height: 1px;
    background: var(--ink);
  }
  .lid-label .spec {
    position: absolute;
    left: 0; right: 0;
    font-size: 9.5px;
    line-height: 1;
  }
  .lid-label .hold { top: 265px; }
  .lid-label .weight { top: 279px; }
</style>
</head>
<body>
  <section class="side-label">
    <div class="wordmark">BRANT</div>
    <div class="divider"></div>
    <ul class="claims">
      <li>Naturally derived plant &amp; bee-based ingredients</li>
      <li>Alcohol Free, Non-Irritating</li>
      <li>Formulated to minimize scalp irritation</li>
    </ul>
  </section>

  <section class="lid-label">
    <div class="wordmark">BRANT</div>
    <div class="product">HAIR POMADE</div>
    <div class="scent">Fresh &amp; Clean</div>
    <div class="rule"></div>
    <div class="spec hold">Medium Hold – Matte Finish</div>
    <div class="spec weight">NET WT 2 oz (57 g)</div>
  </section>
</body>
</html>
```